Business Card Design Project

Business card for law firm
Use existing logo
Must have:
Gerald P. Whitcombe
2715-C West 6th
Riverton, NM 78521
gwhitcombe@dvlegalgroup.com
www.dvlegalgroup.com
555-412-3095

Target Market(s)

Clients and potential clients, generally adult, business background

Industry/Entity Type

Business

Requirements
Must have
• Our logo, see below

```html
<!DOCTYPE html>
<html lang="en">
<head>
<meta charset="utf-8">
<title>Delvecchio Vance — Business Card</title>
<link rel="stylesheet" href="https://fonts.googleapis.com/css2?family=Marcellus&family=Marcellus+SC&display=swap">
<style>
  :root {
    --page-bg: #e9e9e8;
    --card-light: #c3c4c6;
    --card-mid: #707173;
    --card-dark: #2e2e30;
    --card-white: #ffffff;
    --tagline: #5a5b5d;
    --contact-text: #e6e6e6;
  }
  html, body {
    margin: 0;
    padding: 0;
    width: 1200px;
    height: 840px;
    overflow: hidden;
    background: var(--page-bg);
  }
  .stage {
    width: 1200px;
    height: 840px;
    display: flex;
    align-items: center;
    justify-content: center;
  }
  .business-card {
    width: 840px;
    height: 480px;
    display: block;
    box-shadow: 0 10px 30px rgba(0, 0, 0, 0.18);
    font-family: "Marcellus SC", "Times New Roman", serif;
  }
  .panel-light { fill: var(--card-light); }
  .panel-white { fill: var(--card-white); }
  .panel-mid { fill: var(--card-mid); }
  .panel-dark { fill: var(--card-dark); }
  .firm-name {
    font-family: "Marcellus", "Times New Roman", serif;
    fill: var(--card-dark);
    font-size: 30px;
    letter-spacing: 0.5px;
  }
  .firm-tagline {
    font-family: "Marcellus", "Times New Roman", serif;
    fill: var(--tagline);
    font-size: 14px;
    letter-spacing: 2px;
  }
  .contact { fill: var(--contact-text); }
  .contact-name {
    font-size: 18px;
    letter-spacing: 1px;
    fill: var(--card-white);
  }
  .contact-line {
    font-size: 14px;
    letter-spacing: 0.8px;
  }
</style>
</head>
<body>
<main class="stage">
  <svg class="business-card" viewBox="0 0 840 480" xmlns="http://www.w3.org/2000/svg" aria-label="Delvecchio Vance business card for Gerald P. Whitcombe">
    <rect class="panel-white" x="0" y="0" width="840" height="480"/>
    <polygon class="panel-light" points="0,0 840,0 840,95 0,215"/>
    <polygon class="panel-mid" points="240,261 500,224 400,480 340,480"/>
    <polygon class="panel-dark" points="560,215 840,175 840,480 460,480"/>

    <g class="firm-identity" transform="rotate(-8.13 40 210)">
      <text class="firm-name" x="40" y="199">Delvecchio Vance</text>
      <text class="firm-tagline" x="41" y="222">ATTORNEYS AT LAW</text>
    </g>

    <g class="contact">
      <text class="contact-name" x="566" y="272">Gerald P. Whitcombe</text>
      <text class="contact-line" x="566" y="300">2715-C West 6th</text>
      <text class="contact-line" x="566" y="324">Riverton, NM 78521</text>
      <text class="contact-line" x="566" y="348">gwhitcombe@dvlegalgroup.com</text>
      <text class="contact-line" x="566" y="372">www.dvlegalgroup.com</text>
      <text class="contact-line" x="566" y="396">555-412-3095</text>
    </g>
  </svg>
</main>
</body>
</html>
```